Civil Engineering Web design

.Net Web design for a civil engineering company to include a blog page, I will like a site similar to this http://www.layoutgrove.example/demo/58273.html

company name: Dorvil Associates

-Civil/Structural Engineering Solutions

-Engineering Design Development and Consultancy

More Information about the internal pages or links:
1. Each one of the menu choices will take you to a page for that option where I will be able to insert text 2. Our team likewise should be a page with space for a photo of the staff and text space for inserting employee name and title, qualifications and job description and work experience...
Can we have 3 groups for these
Management Staff
Support Staff
Other Staff

3. The blog is a generic blog page where users can add comments to a any subjects raised by our team and submit... When they submit, the comments should be emailed to us 4. Contact us is also a tool for emailing us by users, whereby they provide their email, subject and email body 5. projects is a page that allows insertion of title, one photo and description of the project...
6. services is a page with links on the left for Construction Supervision Civil and Structured Engineering Designs Corporate Recognition

Each on when clicked should display the relevant information for the link which is a gallery of two photos side by side and one description per pair...

Industry/Entity Type

Construction

Requirements
Must have
• User ability to manage content; not design

Pages:
Home
Services
Projects (sub page picture gallery)
Reference
Our Team
Blog
Contact Us

```html
<!DOCTYPE html>
<html lang="en">
<head>
<meta charset="utf-8">
<title>Tavro Civil Engineering</title>
<link rel="stylesheet" href="https://fonts.googleapis.com/css2?family=Archivo:wght@800&family=Roboto+Condensed:wght@400&family=Arimo:wght@400&display=swap">
<style>
  :root {
    --red: #c8172c;
    --red-soft: rgba(200, 23, 44, 0.85);
    --ink: #111111;
    --panel: rgba(28, 30, 34, 0.88);
    --nav-text: #9a9a9a;
    --white: #ffffff;
    --muted: #8a8a8a;
    --rule: rgba(255, 255, 255, 0.12);
  }
  * { margin: 0; padding: 0; box-sizing: border-box; }
  html, body { width: 1200px; height: 681px; overflow: hidden; background: var(--ink); }
  .site { position: relative; width: 1200px; height: 681px; overflow: hidden; font-family: "Arimo", Arial, sans-serif; }

  .hero-photo {
    position: absolute; left: 0; top: 0; width: 1200px; height: 578px;
    background: linear-gradient(100deg, #2e3440 0%, #3a3f4c 30%, #4a2a34 50%, #2c3242 70%, #4b5060 100%);
  }

  .brand {
    position: absolute; left: 0; top: 0; width: 171px; height: 75px;
    background: var(--red); color: var(--white);
    font-family: "Archivo", Arial, sans-serif; font-weight: 800; font-size: 40px;
    letter-spacing: -2px; text-align: right; padding: 20px 11px 0 0; line-height: 1;
  }

  .main-nav { position: absolute; left: 0; top: 84px; width: 171px; list-style: none; }
  .main-nav li {
    height: 41px; background: var(--panel); border-right: 4px solid var(--red);
    border-bottom: 1px solid var(--rule);
    font-family: "Roboto Condensed", Arial, sans-serif; font-size: 17px; color: var(--nav-text);
    text-transform: uppercase; text-align: right; padding: 10px 21px 0 0;
  }
  .main-nav li.is-active { background: var(--red); color: var(--white); }

  .hero-title {
    position: absolute; left: 249px; top: 192px;
    font-family: "Archivo", Arial, sans-serif; font-weight: 800; letter-spacing: -4px; line-height: 80px;
  }
  .hero-title .name { display: block; color: var(--white); font-size: 86px; }
  .hero-title .tagline { display: block; color: var(--red); font-size: 82px; letter-spacing: -5px; }

  .slider-arrows { position: absolute; left: 561px; top: 406px; display: flex; gap: 2px; }
  .slider-arrows span { width: 41px; height: 41px; background: rgba(200, 23, 44, 0.45); display: flex; align-items: center; justify-content: center; }

  .recent-label {
    position: absolute; left: 0; top: 447px; width: 138px; height: 131px; background: var(--panel);
    color: var(--white); font-family: "Roboto Condensed", Arial, sans-serif; font-size: 14px;
    text-transform: uppercase; text-align: center; padding-top: 25px;
  }
  .recent-label .pager { display: block; margin-top: 6px; padding-left: 38px; }

  .recent-post { position: absolute; left: 138px; top: 447px; width: 507px; height: 131px; background: var(--red-soft); padding: 27px 25px 0 26px; color: var(--white); }
  .recent-post h2 { font-family: "Roboto Condensed", Arial, sans-serif; font-weight: 400; font-size: 14px; text-transform: uppercase; margin-bottom: 6px; }
  .recent-post p { font-size: 10.5px; line-height: 20px; }

  .site-footer { position: absolute; left: 0; top: 578px; width: 1200px; height: 103px; background: var(--ink); }
  .footer-nav { position: absolute; left: 25px; top: 36px; display: flex; gap: 23px; list-style: none; }
  .footer-nav li, .copyright { font-size: 8.5px; letter-spacing: 1.5px; color: var(--muted); text-transform: uppercase; }
  .copyright { position: absolute; left: 25px; top: 58px; }
  .social { position: absolute; left: 756px; top: 33px; }
  .footer-code { position: absolute; left: 942px; top: 44px; font-size: 11px; color: var(--muted); letter-spacing: 1px; }
</style>
</head>
<body>
<div class="site">
  <div class="hero-photo" role="img" aria-label="Photo of a construction worker laying pipes on a building site"></div>

  <div class="brand">Tavro</div>

  <ul class="main-nav">
    <li>Home</li>
    <li>Services</li>
    <li>Projects</li>
    <li>Reference</li>
    <li>Our Team</li>
    <li class="is-active">Blog</li>
    <li>Contact Us</li>
  </ul>

  <h1 class="hero-title">
    <span class="name">Tavro</span>
    <span class="tagline">civil engineering</span>
  </h1>

  <div class="slider-arrows">
    <span><svg width="14" height="22" viewBox="0 0 14 22"><polyline points="12,1 2,11 12,21" fill="none" stroke="#d9a0a8" stroke-width="1.5"/></svg></span>
    <span><svg width="14" height="22" viewBox="0 0 14 22"><polyline points="2,1 12,11 2,21" fill="none" stroke="#d9a0a8" stroke-width="1.5"/></svg></span>
  </div>

  <div class="recent-label">
    Recent Posts
    <span class="pager"><svg width="22" height="8" viewBox="0 0 22 8"><polyline points="5,1 2,4 5,7" fill="none" stroke="#999" stroke-width="1"/><polyline points="16,1 19,4 16,7" fill="none" stroke="#999" stroke-width="1"/></svg></span>
  </div>

  <article class="recent-post">
    <h2>It is a long established fact that a reader will be distracted</h2>
    <p>It is a long established fact that a reader will be distracted by the readable content of a page when looking at its layout. The point of using Lorem Ipsum is that it has a more-or-less normal distribu-tion of letters, as opposed...</p>
  </article>

  <footer class="site-footer">
    <ul class="footer-nav">
      <li>Home</li><li>Services</li><li>Projects</li><li>Reference</li><li>Our Team</li><li>Blog</li><li>Contact Us</li>
    </ul>
    <p class="copyright">2014 Tavro | All Rights Reserved</p>
    <svg class="social" width="102" height="32" viewBox="0 0 102 32" aria-label="Social links">
      <circle cx="15" cy="16" r="14" fill="none" stroke="#444" stroke-width="1.2"/>
      <circle cx="50" cy="16" r="14" fill="none" stroke="#444" stroke-width="1.2"/>
      <circle cx="85" cy="16" r="14" fill="none" stroke="#444" stroke-width="1.2"/>
    </svg>
    <span class="footer-code">C8</span>
  </footer>
</div>
</body>
</html>
```